Business card for massage therapy company called Brook Fern Wellness

Need business card for massage therapy company called Brook Fern Wellness. Would like my logo on the front and the back of the card I have 3 options of logos and you can play with what looks better.

Would like this information displayed on the back of the card:

Marcus Ellery
Licensed Massage Therapist
321-555-0147
brookfern-example.com
brookfern_rest_

```html
<!DOCTYPE html>
<html lang="en">
<head>
<meta charset="utf-8">
<title>Brook Fern Wellness — Business Card</title>
<link rel="stylesheet" href="https://fonts.googleapis.com/css2?family=Josefin+Sans:wght@300&family=Montserrat:wght@500&family=Arimo:wght@400&display=swap">
<style>
  :root {
    --backdrop: #5a5a5a;
    --card: #2e2e2e;
    --sage: #727a62;
    --tan: #b98a68;
    --ink-light: #f2f2f2;
  }
  * { margin: 0; padding: 0; box-sizing: border-box; }
  html, body {
    width: 1200px;
    height: 1200px;
    overflow: hidden;
    background: var(--backdrop);
  }
  .card {
    position: absolute;
    left: 255px;
    width: 690px;
    height: 394px;
    background: var(--card);
  }
  .card--front { top: 158px; }
  .card--back { top: 652px; }

  .brand-name {
    font-family: "Josefin Sans", sans-serif;
    font-weight: 300;
    color: var(--sage);
    text-transform: uppercase;
  }
  .front-brand {
    position: absolute;
    left: 35px;
    top: 70px;
    font-size: 30px;
    line-height: 1.15;
    letter-spacing: 2px;
  }
  .holder-name {
    position: absolute;
    left: 35px;
    top: 180px;
    font-family: "Montserrat", sans-serif;
    font-weight: 500;
    font-size: 24px;
    letter-spacing: 0.5px;
    color: var(--tan);
  }
  .holder-role {
    position: absolute;
    left: 35px;
    top: 211px;
    font-family: "Arimo", sans-serif;
    font-size: 14.5px;
    color: var(--sage);
  }
  .address {
    position: absolute;
    left: 37px;
    top: 243px;
    font-family: "Arimo", sans-serif;
    font-size: 15.5px;
    line-height: 21px;
    color: var(--ink-light);
    font-style: normal;
  }
  .contact-list {
    position: absolute;
    left: 37px;
    top: 297px;
    list-style: none;
    font-family: "Arimo", sans-serif;
    font-size: 15.5px;
    color: var(--ink-light);
  }
  .contact-list li {
    display: flex;
    align-items: center;
    height: 21px;
  }
  .contact-icon {
    width: 14px;
    height: 14px;
    margin-right: 12px;
    fill: var(--tan);
  }
  .emblem {
    position: absolute;
    left: 305px;
    top: 41px;
    width: 312px;
    height: 312px;
    border: 2.5px solid var(--sage);
    border-radius: 50%;
    display: flex;
    align-items: center;
    justify-content: center;
    text-align: center;
  }
  .emblem .brand-name {
    font-size: 28px;
    line-height: 1.25;
    letter-spacing: 3px;
  }

  .back-mark {
    position: absolute;
    left: 282px;
    top: 82px;
    width: 134px;
    height: 134px;
    border: 1.5px solid var(--sage);
    border-radius: 50%;
  }
  .back-brand {
    position: absolute;
    left: 0;
    right: 0;
    top: 225px;
    text-align: center;
    line-height: 1;
  }
  .back-brand .line-main {
    display: block;
    font-size: 44px;
    letter-spacing: 3px;
  }
  .back-brand .line-sub {
    display: block;
    margin-top: 10px;
    font-size: 23px;
    letter-spacing: 9px;
  }
</style>
</head>
<body>
  <section class="card card--front">
    <div class="brand-name front-brand">Brook Fern<br>Wellness</div>
    <h1 class="holder-name">MARCUS ELLERY</h1>
    <p class="holder-role">Licensed Massage Therapist</p>
    <address class="address">412 Alder Way<br>Riverton, Canada 10423</address>
    <ul class="contact-list">
      <li>
        <svg class="contact-icon" viewBox="0 0 24 24" aria-hidden="true"><path d="M6.6 10.8a15.2 15.2 0 0 0 6.6 6.6l2.2-2.2a1 1 0 0 1 1-.25 11.4 11.4 0 0 0 3.6.57 1 1 0 0 1 1 1V20a1 1 0 0 1-1 1A17 17 0 0 1 3 4a1 1 0 0 1 1-1h3.5a1 1 0 0 1 1 1c0 1.25.2 2.45.57 3.6a1 1 0 0 1-.25 1z"/></svg>
        321-555-0147
      </li>
      <li>
        <svg class="contact-icon" viewBox="0 0 24 24" aria-hidden="true"><path d="M2 6h20v12H2z M2 6l10 7 10-7" fill="none" stroke="#b98a68" stroke-width="2"/><path d="M2 7l10 7 10-7v11H2z"/></svg>
        info@brookfern-example.com
      </li>
      <li>
        <svg class="contact-icon" viewBox="0 0 24 24" aria-hidden="true"><circle cx="12" cy="12" r="10"/><path d="M7 7c2 0 3 1 3 3s-2 2-2 4 2 3 2 5M15 4c0 2 1 3 3 3M14 14c2 0 3 1 3 3" fill="none" stroke="#2e2e2e" stroke-width="1.8"/></svg>
        www.brookfern-example.com
      </li>
    </ul>
    <div class="emblem">
      <span class="brand-name">Brook Fern<br>Wellness</span>
    </div>
  </section>

  <section class="card card--back">
    <div class="back-mark"></div>
    <div class="brand-name back-brand">
      <span class="line-main">Brook Fern</span>
      <span class="line-sub">Wellness</span>
    </div>
  </section>
</body>
</html>
```